Letterhead Design Project (logo provided)

We are a legal services provider company called VRN Legal based in the UK and would like some letterhead paper designed.

The design should use the attached logo, and should use the colors feature in the logo (along with blacks and/or greys).

The background paper must be white - and A4 size.

The letterhead should be provided in both .pdf and .doc (or .odf) formats.

Target Market(s)

Customers and clients for legal services

Industry/Entity Type

Legal

Requirements
Must have
• The header must include the following information:

Business name - VRN Legal LLP
Office address - Larchmead Court, Wallingford, Oxfordshire OX10 4TL, United Kingdom
Telephone - +44 (0)1491 736480
Email - mail@ [domain given below]
Website: www.vrnlegal-example.com

The footer must include the following information:

Registered office address - 14 Alder Row, Brindlecote, Wallingford, Oxfordshire OX10 6QD, United Kingdom
Companies House registration number - OC718463
VAT registration number - GB 417386205

```html
<!DOCTYPE html>
<html lang="en">
<head>
<meta charset="utf-8">
<title>VRN Legal LLP – Letterhead</title>
<link href="https://fonts.googleapis.com/css2?family=Arimo:wght@400;700&display=swap" rel="stylesheet">
<style>
  :root {
    --green: #3fb54b;
    --green-light: #8fd08f;
    --navy: #1d4f8f;
    --ink: #3a3a3a;
    --white: #ffffff;
  }
  * { margin: 0; padding: 0; box-sizing: border-box; }
  html, body { width: 857px; height: 1200px; overflow: hidden; background: var(--white); }
  .letterhead {
    position: relative;
    width: 857px;
    height: 1200px;
    background: var(--white);
    font-family: "Arimo", Arial, sans-serif;
    color: var(--ink);
  }
  .header-band {
    position: absolute;
    top: 0; left: 0;
    width: 857px; height: 290px;
  }
  .brand {
    position: absolute;
    left: 30px; top: 58px;
    display: flex; align-items: center; gap: 12px;
  }
  .brand-mark {
    width: 22px; height: 22px; border-radius: 50%;
    background: var(--green);
  }
  .brand-name {
    font-size: 54px; font-weight: 400;
    color: var(--navy); letter-spacing: 1px;
    white-space: nowrap;
  }
  .header-contact {
    position: absolute;
    right: 26px; top: 34px;
    text-align: right;
    color: var(--white);
    font-size: 14.5px; line-height: 18px;
  }
  .header-contact .address { margin-bottom: 22px; }
  .footer {
    position: absolute;
    left: 0; right: 0; top: 1086px;
    font-size: 14px; line-height: 17px;
  }
  .registered-office {
    position: absolute;
    left: 70px; width: 250px;
    text-align: center;
  }
  .registered-office h2 {
    font-size: 17px; font-weight: 700; color: var(--ink);
    margin-bottom: 5px;
  }
  .registration {
    position: absolute;
    left: 445px; top: 30px;
  }
</style>
</head>
<body>
<div class="letterhead">
  <svg class="header-band" viewBox="0 0 857 290" aria-hidden="true">
    <path d="M330 0 C360 90 420 150 470 190 C510 222 545 232 575 234 L857 234 L857 244 L560 244 C490 238 420 180 380 110 C360 75 345 40 330 0 Z" fill="var(--green-light)"/>
    <path d="M345 0 L857 0 L857 228 L580 228 C520 226 470 200 430 150 C395 105 370 55 345 0 Z" fill="var(--green)"/>
  </svg>

  <div class="brand">
    <span class="brand-name">VRN Legal</span>
    <span class="brand-mark"></span>
  </div>

  <div class="header-contact">
    <p class="address">Larchmead Court, Wallingford,<br>Oxfordshire OX10 4TL,<br>United Kingdom.</p>
    <p class="contact">Tele: +44 (0)1491 736480<br>Email: mail@vrnlegal-example.com<br>Website: www.vrnlegal-example.com</p>
  </div>

  <footer class="footer">
    <div class="registered-office">
      <h2>Registered Office Address</h2>
      <p>14 Alder Row, Brindlecote,<br>Wallingford, Oxfordshire OX10 6QD,<br>United Kingdom</p>
    </div>
    <div class="registration">
      <p>Companies House registration number - OC718463</p>
      <p>VAT registration number - GB 417386205</p>
    </div>
  </footer>
</div>
</body>
</html>
```